Anzeigengestaltung für Fliesenlegermeister
Zielgruppe
Ich bin ein Fliesenlegermeister und möchte mich selbstständig machen, ich saniere Bäder, Böden mit Fliesen, Fliesenspiegel und ich möchte eine Anzeige in den regionalen Zeitungen machen. Ich spreche alle Altersklassen mit Bädern für Sanierungen, Bodenfliesen und Neubauten an. Reparatur und Silikonarbeiten sowie Trockenbauarbeiten am eigenen Heim .
Aufgabenstellung
Ich möchte gern meine Kontaktdaten und die Farben vom Logo wieder finden,
als Beispiel habe ich meine aktuelle Visitenkarte beigefügt Dort finden sich die Kontaktdaten. Meine Arbeiten sind insbesondere :
Fliesenverlegung
Badsanierung
barrierefreie Bäder
Reparaturarbeiten
Silikonarbeiten
Trockenbau
Ob nun genau alle 6 Punkte in der Anzeige angezeigt werden soll bin ich mir nicht sicher oder ob nur 4 Beschreibungen reichen, damit es nicht zu viel wird.

```html
<!DOCTYPE html>
<html lang="de">
<head>
<meta charset="utf-8">
<title>Fliesenlegermeister Jonas Berland – Anzeige</title>
<link href="https://fonts.googleapis.com/css2?family=Rajdhani:wght@600;700&family=Roboto:wght@400;500;700&display=swap" rel="stylesheet">
<style>
  :root{
    --ink:#4a4a4c;
    --frame:#4a4a4a;
    --line:#d2d2d4;
    --blue:#0d51a0;
    --bar:#4b4b4d;
    --white:#ffffff;
    --tile-light:#e4c4a0;
    --tile-dark:#c8916c;
  }
  *{box-sizing:border-box;margin:0;padding:0}
  html,body{width:1200px;height:1200px;overflow:hidden;background:var(--white)}
  body{position:relative;font-family:"Roboto",sans-serif;color:var(--ink)}
  .ad{
    position:absolute;left:292px;top:257px;width:892px;height:990px;
    transform:scale(0.6918);transform-origin:top left;
    border:6px solid var(--frame);background:var(--white);overflow:hidden;
  }
  .ad > *{position:absolute}
  .hero-photo{
    left:0;top:0;width:880px;height:240px;
    background:linear-gradient(160deg,#d9a98a 0%,var(--tile-light) 45%,#e9cfb2 70%,var(--tile-dark) 100%);
    clip-path:polygon(0 0,100% 0,100% 204px,61% 206px,50% 236px,34% 206px,0 204px);
  }
  .guides{left:0;top:0;width:880px;height:978px}
  .headline{
    left:152px;top:267px;width:576px;height:125px;
    border:14px solid var(--line);border-radius:22px;background:var(--white);
    font-family:"Rajdhani",sans-serif;font-weight:600;font-size:47px;line-height:44px;
    text-align:center;display:flex;flex-direction:column;justify-content:center;letter-spacing:1.2px;
    white-space:nowrap;
  }
  .services{left:14px;top:428px;list-style:none}
  .services li{
    font-weight:700;font-size:41px;line-height:50px;padding-left:50px;position:relative;white-space:nowrap;
  }
  .services li::before{
    content:"";position:absolute;left:8px;top:16px;width:18px;height:18px;
    background:var(--blue);transform:rotate(45deg);
  }
  .phone-bar{
    left:448px;width:432px;height:80px;background:var(--bar);color:var(--white);
    font-weight:700;font-size:46px;display:flex;align-items:center;justify-content:space-between;
    padding:0 14px 0 8px;white-space:nowrap;
  }
  .phone-bar.landline{top:434px}
  .phone-bar.mobile{top:525px}
  .phone-bar svg{width:48px;height:52px}
  .address{left:456px;top:628px;display:flex;gap:12px;font-size:30px;line-height:37px;font-style:normal}
  .address svg{width:32px;height:52px;margin-top:4px}
  .brand{left:400px;top:774px;display:flex;align-items:center;gap:18px}
  .brand-square{width:46px;height:46px;background:var(--blue)}
  .brand-name{font-weight:700;font-size:50px;color:var(--blue);letter-spacing:1px;white-space:nowrap}
  .mail-band{
    left:0;top:884px;width:880px;height:94px;background:var(--blue);
    clip-path:polygon(237px 0,100% 0,100% 100%,132px 100%);
  }
  .mail{
    left:236px;top:908px;color:var(--white);font-size:38px;line-height:46px;font-weight:500;white-space:nowrap;
  }
  .sticker{
    left:38px;top:744px;width:204px;height:204px;border-radius:50%;background:var(--blue);
    color:var(--white);display:flex;align-items:center;justify-content:center;
  }
  .sticker p{
    transform:rotate(-24deg);font-weight:700;font-size:25px;line-height:25px;text-align:center;
  }
</style>
</head>
<body>
  <section class="ad">
    <div class="hero-photo" role="img" aria-label="Foto: Hand zeichnet mit Bleistift und Winkel eine Linie auf eine Bodenfliese"></div>

    <svg class="guides" viewBox="0 0 880 978" aria-hidden="true">
      <polyline points="340,210 440,250 440,280" fill="none" stroke="var(--line)" stroke-width="14"/>
      <polyline points="440,390 440,676 140,990" fill="none" stroke="var(--line)" stroke-width="14"/>
    </svg>

    <h1 class="headline"><span>PROFESSIONELLER</span><span>FLIESENLEGERMEISTER</span></h1>

    <ul class="services">
      <li>Fliesenverlegung</li>
      <li>Badsanierung</li>
      <li>barrierefreie Bäder</li>
      <li>Reparaturarbeiten</li>
      <li>Silikonarbeiten</li>
      <li>Trockenbau</li>
    </ul>

    <div class="phone-bar landline">
      <svg viewBox="0 0 48 52" aria-hidden="true" fill="none" stroke="#fff" stroke-width="2.2" stroke-linecap="round">
        <path d="M10 14c-4 4-2 12 6 20s16 11 20 7l3-3-7-7-4 3c-3-1-8-6-9-9l3-4-7-7z"/>
        <path d="M28 10a12 12 0 0 1 10 10M28 4a18 18 0 0 1 16 16"/>
      </svg>
      <span>05321/4807615</span>
    </div>
    <div class="phone-bar mobile">
      <svg viewBox="0 0 48 52" aria-hidden="true" fill="none" stroke="#fff" stroke-width="2.2">
        <rect x="8" y="4" width="32" height="46" rx="4"/>
        <line x1="8" y1="12" x2="40" y2="12"/><line x1="8" y1="42" x2="40" y2="42"/>
        <circle cx="24" cy="46" r="1.5"/>
      </svg>
      <span>01639254180</span>
    </div>

    <address class="address">
      <svg viewBox="0 0 32 52" aria-hidden="true" fill="none" stroke="var(--ink)" stroke-width="2">
        <path d="M16 40C8 28 3 22 3 15a13 13 0 0 1 26 0c0 7-5 13-13 25z"/>
        <circle cx="16" cy="15" r="5"/>
        <ellipse cx="16" cy="45" rx="6" ry="2.5"/>
      </svg>
      <span>Lindenweg 7, 38100<br>Talbrück</span>
    </address>

    <div class="brand">
      <div class="brand-square"></div>
      <span class="brand-name">JONAS BERLAND</span>
    </div>

    <div class="mail-band"></div>
    <p class="mail">info@fliesenlegermeister-berland.de</p>

    <div class="sticker"><p>JETZT<br>TERMIN<br>VEREINBAREN</p></div>
  </section>
</body>
</html>
```